Flyer
Der Flyer ist super geworden. Vielen Dank! :-)
Zielgruppe
Wir sind Hersteller von Unterkonstruktion für PV-Anlagen. Unsere Zielgruppe sind Monteure oder Firmen die PV-Anlagen verbauen.
Aufgabenstellung
Ich hätte gerne einen Slogan wie Bestpreisgarantie. Oder: Unterkonstruktionen in bester Qualität – zum besten Preis
Oder Sie haben selbst Vorschläge; Wenn möglich können Sie gerne die Bilder von der pptx Datei nehmen. Wir haben auf den Clip unter der Hammerkopfschraube ein Patent (liegt bei), dieser Clip ist ein deutlicher Vorteil bei der Verbauung, damit sich die Hammerkopfschraube beim Verbauen nicht verdreht.
Unsere Adresse sollte noch auf den Flyer:
KD Lumatrix Werke GmbH, Falkenhainweg 14, 80417 München
Fon: 089 518 327 40 Mail: info@kdlumatrixwerke.com
Website: www.kdlumatrixwerke.com

```html
<!DOCTYPE html>
<html lang="de">
<head>
<meta charset="utf-8">
<title>KD Lumatrix Werke – Flyer</title>
<link rel="stylesheet" href="https://fonts.googleapis.com/css2?family=Playfair+Display:wght@700&family=Poppins:wght@800&family=Lato:wght@400;700&family=Barlow+Condensed:wght@500&display=swap">
<style>
  :root {
    --navy: #1f2f4f;
    --ink: #2a2a2e;
    --yellow: #edbf32;
    --gold: #d6a82a;
    --footer: #2b2a31;
    --white: #ffffff;
    --badge: #f5f4f0;
    --hero-top: #36466b;
    --hero-bottom: #1e2a4a;
  }
  * { margin: 0; padding: 0; box-sizing: border-box; }
  html, body { width: 848px; height: 1200px; overflow: hidden; background: var(--white); }
  .flyer { position: relative; width: 848px; height: 1200px; background: var(--white); font-family: "Lato", sans-serif; color: var(--ink); }

  .brand { position: absolute; left: 52px; top: 104px; font-family: "Barlow Condensed", sans-serif; font-weight: 500; font-size: 21px; letter-spacing: 0.02em; color: var(--navy); }
  .brand-mark { position: absolute; left: 106px; top: 56px; width: 40px; height: 40px; background: var(--navy); }

  .top-contact { position: absolute; right: 57px; top: 76px; text-align: right; font-size: 13px; line-height: 17.5px; color: var(--navy); }

  .hero-photo { position: absolute; left: 0; top: 181px; width: 848px; height: 475px;
    background: linear-gradient(180deg, var(--hero-top) 0%, var(--hero-bottom) 100%); }
  .hero-title { position: absolute; right: 421px; top: 418px; z-index: 2; text-align: right; font-family: "Playfair Display", serif; font-weight: 700; color: var(--white); line-height: 51px; }
  .hero-title .lead { font-size: 49px; display: block; }
  .hero-title .rest { font-size: 36px; display: block; }
  .hero-bar { position: absolute; left: 49px; top: 606px; width: 396px; height: 26px; border-radius: 14px 14px 0 0; background: linear-gradient(90deg, var(--yellow), var(--gold)); }

  .slogan-box { position: absolute; left: 509px; top: 387px; width: 339px; height: 306px; background: var(--yellow); border-top-left-radius: 33px; }
  .slogan { position: absolute; left: 77px; top: 40px; font-family: "Poppins", sans-serif; font-weight: 800; font-size: 44px; line-height: 37.5px; color: var(--white); }
  .quote-mark { position: absolute; left: 237px; top: 235px; width: 48px; height: 46px; }

  .gear { position: absolute; left: 52px; top: 668px; width: 34px; height: 34px; }
  .section-title { position: absolute; left: 49px; top: 706px; font-family: "Playfair Display", serif; font-weight: 700; font-size: 32px; color: var(--ink); }
  .section-body { position: absolute; left: 54px; top: 762px; width: 735px; font-size: 13px; line-height: 21.5px; letter-spacing: 0.105em; color: var(--ink); }

  .footer { position: absolute; left: 0; top: 952px; width: 848px; height: 248px; background: var(--footer); color: var(--white); }
  .badge { position: absolute; width: 78px; height: 78px; border-radius: 50%; background: var(--badge); top: 49px; }
  .badge.large { width: 133px; height: 133px; top: -5px; }
  .address { position: absolute; top: 152px; width: 100%; text-align: center; font-size: 14.5px; letter-spacing: 0.06em; }
  .rule { position: absolute; left: 49px; top: 183px; width: 735px; height: 1px; background: var(--white); }
  .footer-contact { position: absolute; top: 196px; width: 100%; text-align: center; font-size: 14.5px; letter-spacing: 0.08em; }
  .footer-contact .sep { margin: 0 8px; }
  .footer-contact strong { font-weight: 700; }
</style>
</head>
<body>
<div class="flyer">
  <header>
    <div class="brand-mark"></div>
    <div class="brand">KD LUMATRIX WERKE</div>
    <div class="top-contact">
      089 518 327 40<br>
      info@kdlumatrixwerke.com<br>
      www.kdlumatrixwerke.com
    </div>
  </header>

  <section class="hero">
    <div class="hero-photo" role="img" aria-label="Foto: Reihen von Solarmodulen auf einem Freiflächen-Feld"></div>
    <div class="hero-bar"></div>
    <h1 class="hero-title">
      <span class="lead">Nachhaltige</span>
      <span class="rest">Unterkonstruktionen</span>
      <span class="rest">für eine standhafte</span>
      <span class="rest">Zukunft</span>
    </h1>
    <div class="slogan-box">
      <p class="slogan">Beste<br>Qualität<br>zum<br>besten<br>Preis</p>
      <svg class="quote-mark" viewBox="0 0 48 46" aria-hidden="true">
        <path d="M10 0h14c-2 16-8 32-20 46H0c6-10 9-20 10-30z" fill="var(--ink)"/>
        <path d="M32 0h14c-2 16-8 32-20 46h-4c6-10 9-20 10-30z" fill="var(--ink)"/>
      </svg>
    </div>
  </section>

  <section class="system">
    <svg class="gear" viewBox="0 0 34 34" aria-hidden="true">
      <g fill="var(--yellow)">
        <rect x="13" y="0" width="8" height="34" rx="1"/>
        <rect x="0" y="13" width="34" height="8" rx="1"/>
        <rect x="13" y="0" width="8" height="34" rx="1" transform="rotate(45 17 17)"/>
        <rect x="13" y="0" width="8" height="34" rx="1" transform="rotate(-45 17 17)"/>
        <circle cx="17" cy="17" r="12"/>
      </g>
      <circle cx="17" cy="17" r="5.5" fill="var(--white)"/>
    </svg>
    <h2 class="section-title">Unser Montagesystem:</h2>
    <p class="section-body">
      Sicherer Verschluss und Verbindung der Dachhaken mit den Profilschienen.<br>
      Durch den speziell entwickelten Kunststoff-Clip wird die Hammerkopfschraube immer korrekt<br>positioniert (90° zur Profilschiene).<br>
      Die Profilschiene mit Hammerkopfschraube ist universell einsetzbar und bietet eine hohe Flexibilität.<br>
      Durch unsere Patente und das Gebrauchsmuster können wir die Montagezeit enorm reduzieren.
    </p>
  </section>

  <footer class="footer">
    <div class="badge" style="left:52px" role="img" aria-label="Zertifikat"></div>
    <div class="badge" style="left:175px" role="img" aria-label="Garantie-Siegel"></div>
    <div class="badge" style="left:299px" role="img" aria-label="Zertifikat"></div>
    <div class="badge" style="left:423px" role="img" aria-label="Zertifikat"></div>
    <div class="badge large" style="left:545px" role="img" aria-label="Zertifikat"></div>
    <div class="badge" style="left:715px" role="img" aria-label="Zertifikat"></div>
    <p class="address">KD Lumatrix Werke GmbH, Falkenhainweg 14, 80417 München</p>
    <div class="rule"></div>
    <p class="footer-contact">089 518 327 40<span class="sep">·</span>info@kdlumatrixwerke.com<span class="sep">·</span><strong>www.kdlumatrixwerke.com</strong></p>
  </footer>
</div>
</body>
</html>
```